Website design for an Italian restaurant in Amsterdam

I need a design for a client of mine. It is for Teatro Lunaverde, an Italian restaurant in Amsterdam.
We are going for a clean, modern look but we also need to realise an authentic feel.
The restaurant is located in an old movie theatre, that is where the name Teatro Lunaverde comes from.
Industry/Entity Type
Italian Restaurant
Number of Pages Required
1 page
Font styles to use
Sans Serif
Colors
Designer to choose colors to be used in the design.

```html
<!DOCTYPE html>
<html lang="en">
<head>
<meta charset="utf-8">
<title>Teatro Lunaverde – Italian Restaurant Amsterdam</title>
<link rel="stylesheet" href="https://fonts.googleapis.com/css2?family=Roboto:wght@400;500;700&family=Cinzel:wght@400;700&family=Playball&family=Libre+Baskerville:wght@400;700&display=swap">
<style>
:root{
  --gold:#e2b312;
  --sand:#a58d6a;
  --cream:#ede3da;
  --ink:#333333;
  --crimson:#b8344b;
  --white:#ffffff;
}
*{box-sizing:border-box;margin:0;padding:0}
html,body{width:1200px;height:2862px;overflow:hidden;background:var(--white)}
body{position:relative;font-family:'Roboto',sans-serif;color:var(--ink)}
.abs{position:absolute}

/* header */
.site-header{position:absolute;left:0;top:0;width:1200px;height:109px;background:var(--white)}
.nav a{position:absolute;top:48px;font-size:11px;letter-spacing:.5px;color:#555;text-decoration:none;text-transform:uppercase}
.nav a.active{border:1px solid #aaa;border-radius:4px;padding:4px 10px;top:43px}
.brand{position:absolute;left:450px;top:20px;width:300px;text-align:center}
.brand-dot{display:block;width:34px;height:34px;border-radius:50%;background:var(--crimson);margin:0 auto 8px}
.brand-name{font-family:'Cinzel',serif;font-weight:700;font-size:21px;color:#222;letter-spacing:.5px}

/* hero */
.hero{position:absolute;left:0;top:109px;width:1200px;height:482px;background:linear-gradient(120deg,#3a2a18 0%,#6b4d2a 35%,#2b2118 60%,#5a4a36 85%,#3a3024 100%)}
.hero-panel{position:absolute;left:273px;top:91px;width:654px;height:319px;background:rgba(40,30,20,.55);text-align:center;color:var(--white)}
.rule{position:absolute;height:1px;background:currentColor}
.hero-welcome{position:absolute;left:0;width:100%;top:70px;font-family:'Playball',cursive;font-size:66px;color:var(--gold)}
.hero-title{position:absolute;left:0;width:100%;top:152px;font-family:'Cinzel',serif;font-size:48px;letter-spacing:1px}
.hero-sub{position:absolute;left:0;width:100%;top:215px;font-size:15px;line-height:19px}

/* reservation */
.reserve{position:absolute;left:0;top:591px;width:1200px;height:73px;background:var(--sand);color:var(--white)}
.reserve-label{position:absolute;left:182px;top:14px;font-size:20px;font-weight:700;line-height:22px}
.reserve-label small{display:block;font-size:14px;font-weight:400}
.reserve-divider{position:absolute;left:298px;top:10px;width:2px;height:53px;background:var(--white)}
.field-label{position:absolute;top:27px;font-size:15px}
.field{position:absolute;top:20px;height:34px;background:rgba(255,255,255,.25);font-size:13px;color:#f3ecdf;padding:9px 20px}
.field svg{position:absolute;right:12px;top:10px}
.btn-search{position:absolute;left:933px;top:20px;width:78px;height:34px;background:var(--gold);color:var(--white);font-size:13px;text-align:center;line-height:34px}

/* section heads */
.section-title{position:absolute;left:0;width:1200px;text-align:center;font-family:'Libre Baskerville',serif;font-weight:400;font-size:23px;color:#555;letter-spacing:.5px}
.divider{position:absolute;width:76px;height:12px}
.divider::before,.divider::after{content:"";position:absolute;top:5px;width:30px;height:1px;background:#aaa}
.divider::before{left:0}.divider::after{right:0}
.divider i{position:absolute;left:34px;top:2px;width:8px;height:8px;border:1px solid #aaa;border-radius:50%}

/* specials */
.specials{position:absolute;left:202px;top:826px;width:796px;height:321px;display:grid;grid-template-columns:repeat(5,1fr);grid-template-rows:repeat(2,1fr)}
.dish-photo{width:100%;height:100%}
.dish-card{background:linear-gradient(#fafafa,#ececec);text-align:center;padding-top:48px}
.dish-card h3{font-size:13px;font-weight:500;color:#444;letter-spacing:.5px}
.dish-card .mini{width:40px;height:1px;background:#aaa;margin:8px auto}
.dish-card p{font-size:9px;line-height:12px;color:#999;padding:0 30px}

/* menu */
.menu{position:absolute;left:0;top:1244px;width:1200px;height:639px;background:linear-gradient(90deg,#f3f2ef,#fbfbfa 50%,#f3f2ef)}
.menu-still{position:absolute;left:0;top:0;width:210px;height:416px;background:radial-gradient(circle at 30% 40%,#d7a84a 0%,#6aa23c 35%,#c9c3b6 70%,rgba(243,242,239,0) 100%)}
.tabs span{position:absolute;top:146px;font-family:'Libre Baskerville',serif;font-size:12px;color:#777}
.tabs span.active{border:1px solid #999;border-radius:4px;padding:4px 14px;top:142px;color:#555}
.cats{position:absolute;left:258px;top:212px;width:244px}
.cats li{list-style:none;height:43px;line-height:43px;padding-left:53px;font-family:'Libre Baskerville',serif;font-weight:700;font-size:12px;color:#444}
.cats li.active{background:rgba(200,200,200,.35)}
.dishes{position:absolute;left:502px;top:212px;width:439px;height:315px;background:rgba(200,200,200,.35)}
.dish{position:absolute;left:22px;width:400px;font-family:'Libre Baskerville',serif}
.dish h4{font-size:12px;color:#333;line-height:16px}
.dish p{font-size:9.5px;color:#777;line-height:15px;width:290px}
.dish .price{position:absolute;left:335px;top:0;font-size:12px;color:#666}

/* testimonials */
.reviews{position:absolute;left:0;top:1883px;width:1200px;height:288px;background:var(--cream)}
.avatar{position:absolute;border-radius:50%;border:4px solid #fff;background:linear-gradient(#d8d1c8,#b8aea2)}
.review-head{position:absolute;left:445px;top:98px;font-family:'Libre Baskerville',serif;font-weight:700;font-size:14px;color:#333}
.review-text{position:absolute;left:445px;top:124px;width:540px;font-family:'Libre Baskerville',serif;font-size:10px;line-height:17px;color:#555}
.review-by{position:absolute;left:651px;top:184px;font-family:'Libre Baskerville',serif;font-size:10px;font-weight:700;color:#444;line-height:16px}
.rating{position:absolute;left:716px;top:184px;width:100px;height:16px;background:#fff;border-radius:8px;font-size:9px;color:var(--gold);line-height:16px;padding-left:8px;letter-spacing:1px}
.rating em{color:#999;font-style:normal;letter-spacing:0}
.dots{position:absolute;left:570px;top:262px}
.dots i{float:left;width:9px;height:9px;border-radius:50%;background:var(--gold);margin-right:4px}
.dots i.on{background:#fff;border:2px solid var(--gold)}

/* contact */
.contact-title{position:absolute;left:198px;top:2249px;font-family:'Libre Baskerville',serif;font-weight:400;font-size:23px;color:#555}
.input{position:absolute;border:1px solid #e3e3e3;border-radius:3px;font-size:10px;color:#aaa;padding:4px 8px;background:#fff}
.btn-send{position:absolute;left:565px;top:2498px;width:86px;height:23px;background:var(--gold);color:#fff;font-size:12px;font-weight:700;text-align:center;line-height:23px;border-radius:2px}
.social-feed{position:absolute;left:742px;top:2209px;width:273px;height:359px;border:1px solid #ddd;background:#fff;box-shadow:0 1px 4px rgba(0,0,0,.12);overflow:hidden}
.feed-top{height:68px;background:linear-gradient(#3a2c22,#4a3a2e);color:#fff;font-size:10px;padding:6px 8px;position:relative}
.feed-top b{font-size:11px;margin-left:6px}
.feed-top .sq{display:inline-block;width:18px;height:18px;background:#111;border:1px solid #fff;vertical-align:middle}
.feed-top .follow{position:absolute;left:34px;top:28px;background:#fff;color:#444;font-size:8px;padding:1px 4px}
.feed-top .tag{position:absolute;left:8px;top:50px;font-size:8px;color:#ddd}
.feed-photo{height:173px;background:linear-gradient(#4a3a30,#6d5a4a 50%,#7d6c5c)}
.feed-post{padding:8px;font-size:8.5px;color:#333;line-height:11px}
.feed-post .who{font-weight:700;font-size:9.5px;line-height:12px}
.feed-post .when{color:#999;font-size:7.5px;line-height:10px;margin-bottom:6px}
.feed-post .gap{margin-top:6px}
.feed-actions{position:absolute;left:8px;bottom:6px;font-size:8px;line-height:10px;color:#777;border-top:1px solid #eee;width:257px;padding-top:5px}

/* footer */
.site-footer{position:absolute;left:0;top:2629px;width:1200px;height:233px;background:var(--sand);color:#fff}
.footer-brand{position:absolute;left:138px;top:58px;width:300px;text-align:center}
.footer-brand .brand-dot{width:30px;height:30px;background:#fff}
.footer-brand .brand-name{color:#fff;font-size:20px}
.footer-col h5{font-size:17px;font-weight:500;margin-bottom:10px}
.footer-col p{font-size:10px;line-height:20px}
.circle-icon{display:inline-block;width:16px;height:16px;border-radius:50%;background:#fff;margin-right:14px;margin-top:14px}
.footer-line{position:absolute;left:0;top:208px;width:1200px;height:1px;background:rgba(255,255,255,.5)}
.copyright{position:absolute;left:0;top:214px;width:1200px;text-align:center;font-size:9px}
</style>
</head>
<body>

<header class="site-header">
  <nav class="nav">
    <a class="active" style="left:200px">Home</a>
    <a style="left:280px">Menu</a>
    <a style="left:350px">Group Menu</a>
    <a style="left:762px">Reservation</a>
    <a style="left:873px">Contact</a>
    <a style="left:961px">Blog</a>
  </nav>
  <div class="brand">
    <span class="brand-dot"></span>
    <span class="brand-name">TEATRO LUNAVERDE</span>
  </div>
</header>

<section class="hero" role="img" aria-label="Photo of the warmly lit restaurant dining room with string lights and the open kitchen">
  <div class="hero-panel">
    <span class="rule" style="left:188px;top:38px;width:278px"></span>
    <div class="hero-welcome">Welcome to</div>
    <div class="hero-title">TEATRO LUNAVERDE</div>
    <div class="hero-sub">The Italian restaurant located in the heart of<br>Amsterdam</div>
    <span class="rule" style="left:188px;top:282px;width:278px"></span>
  </div>
</section>

<section class="reserve">
  <div class="reserve-label">RESERVE<small>YOUR TABLE</small></div>
  <span class="reserve-divider"></span>
  <span class="field-label" style="left:346px">Guests</span>
  <div class="field" style="left:416px;width:162px">no. of guests
    <svg width="18" height="14" viewBox="0 0 18 14"><circle cx="6" cy="4" r="3" fill="#fff"/><path d="M0 13c0-4 3-5 6-5s6 1 6 5z" fill="#fff"/><circle cx="13" cy="4" r="2.5" fill="#fff"/><path d="M12 8c3 0 6 1 6 5h-5c0-2-1-4-1-5z" fill="#fff"/></svg>
  </div>
  <span class="field-label" style="left:607px">When</span>
  <div class="field" style="left:662px;width:232px">select date
    <svg width="14" height="14" viewBox="0 0 14 14"><rect x="1" y="2" width="12" height="11" fill="none" stroke="#fff" stroke-width="1.5"/><rect x="1" y="2" width="12" height="3" fill="#fff"/><rect x="3" y="0" width="2" height="3" fill="#fff"/><rect x="9" y="0" width="2" height="3" fill="#fff"/></svg>
  </div>
  <div class="btn-search">Search</div>
</section>

<h2 class="section-title" style="top:730px">MONTHLY SPECIAL</h2>
<span class="divider" style="left:562px;top:767px"><i></i></span>

<section class="specials">
  <div class="dish-photo" role="img" aria-label="Photo of farfalle pasta with beef ragù" style="background:radial-gradient(circle,#d9a24a,#8a5a2a 70%,#f0ece6)"></div>
  <div class="dish-card"><h3>LOREM IPSUM</h3><div class="mini"></div><p>Lorem ipsum dolor sit amet, consectetur adipiscing elit. Nunc at.</p></div>
  <div class="dish-photo" role="img" aria-label="Photo of seafood spaghetti with shrimp" style="background:radial-gradient(circle,#d87a4a,#8a4a2a 70%,#3a4a5a)"></div>
  <div class="dish-card"><h3>LOREM IPSUM</h3><div class="mini"></div><p>Lorem ipsum dolor sit amet, consectetur adipiscing elit. Nunc at.</p></div>
  <div class="dish-photo" role="img" aria-label="Photo of spaghetti with meatballs and basil" style="background:radial-gradient(circle,#c33a2a,#7a3a2a 60%,#e8e4dc)"></div>
  <div class="dish-card"><h3>LOREM IPSUM</h3><div class="mini"></div><p>Lorem ipsum dolor sit amet, consectetur adipiscing elit. Nunc at.</p></div>
  <div class="dish-photo" role="img" aria-label="Photo of seared tuna salad with a glass of wine" style="background:radial-gradient(circle,#b8584a,#6a8a3a 55%,#f2f0ec)"></div>
  <div class="dish-card"><h3>LOREM IPSUM</h3><div class="mini"></div><p>Lorem ipsum dolor sit amet, consectetur adipiscing elit. Nunc at.</p></div>
  <div class="dish-photo" role="img" aria-label="Photo of tagliatelle in tomato sauce" style="background:radial-gradient(circle,#e07a3a,#c65a2a 50%,#f4f2ee)"></div>
  <div class="dish-card"><h3>LOREM IPSUM</h3><div class="mini"></div><p>Lorem ipsum dolor sit amet, consectetur adipiscing elit. Nunc at.</p></div>
</section>

<section class="menu">
  <div class="menu-still" role="img" aria-label="Still life of tomatoes, pasta, green pepper and mushrooms on a white wooden table"></div>
  <h2 class="section-title" style="top:58px">MENU</h2>
  <span class="divider" style="left:562px;top:94px"><i></i></span>
  <div class="tabs">
    <span class="active" style="left:388px">Foods</span>
    <span style="left:512px">Beverages</span>
    <span style="left:640px">Wines</span>
    <span style="left:742px">Deserts</span>
  </div>
  <ul class="cats">
    <li>Le Insalate</li>
    <li class="active">Antipasti</li>
    <li>Le Paste</li>
    <li>Il Pesce</li>
    <li>La Carne</li>
    <li>Contorni</li>
    <li>Dolce</li>
  </ul>
  <div class="dishes">
    <div class="dish" style="top:17px"><h4>Pane Burro e Tapanada</h4><p>Bread, garlic butter and olive tapenade</p><span class="price">€ 4,50</span></div>
    <div class="dish" style="top:68px"><h4>Carpaccio di Manzo</h4><p>Thinly sliced tenderloin with a pesto of rocketsalad and parmesancheese</p><span class="price">€ 13,50</span></div>
    <div class="dish" style="top:137px"><h4>Carpaccio di Tonno</h4><p>Thinly sliced tuna with red onion, capers and rocketsalad</p><span class="price">€ 14,50</span></div>
    <div class="dish" style="top:206px"><h4>Vitello Tonnato</h4><p style="width:320px">Thinly sliced veal with Piemonte tunasauce and large capers</p><span class="price">€ 14,75</span></div>
    <div class="dish" style="top:255px"><h4>Antipasto Italiano</h4><p>San Daniele ham, piccante salami, Italian wurst, Italian cheese, burrata en olijven (min. 2 pers.)</p><span class="price">€ 16,00</span></div>
  </div>
</section>

<section class="reviews">
  <div class="avatar" role="img" aria-label="Guest portrait" style="left:97px;top:99px;width:80px;height:80px"></div>
  <div class="avatar" role="img" aria-label="Guest portrait" style="left:300px;top:79px;width:114px;height:114px"></div>
  <div class="avatar" role="img" aria-label="Guest portrait" style="left:1023px;top:99px;width:80px;height:80px"></div>
  <div class="review-head">Lorem ipsum dolor sit amet, consectetur adipiscing elit.</div>
  <p class="review-text">Lorem ipsum dolor sit amet, consectetur adipiscing elit. Proin interdum purus quis suscipit viverra. Etiam ullamcorper leo ac auctor aliquet. Vivamus ac dolor malesuada, viverra libero nec, accumsan ligula.</p>
  <span class="review-by">- Jane Doe</span>
  <span class="rating">★★★★★ <em>5 stars</em></span>
  <div class="dots"><i class="on"></i><i></i><i></i><i></i></div>
</section>

<h2 class="contact-title">CONTACT US</h2>
<span class="divider" style="left:250px;top:2286px"><i></i></span>
<div class="input" style="left:193px;top:2322px;width:232px;height:20px">Name</div>
<div class="input" style="left:437px;top:2322px;width:214px;height:20px">Email</div>
<div class="input" style="left:193px;top:2353px;width:458px;height:133px">Message</div>
<div class="btn-send">SEND</div>

<aside class="social-feed">
  <div class="feed-top">
    <span class="sq"></span><b>Teatro Lunaverde</b>
    <span class="follow">Follow</span>
    <span class="tag">Be the first of your friends to like this</span>
  </div>
  <div class="feed-photo" role="img" aria-label="Photo of the restaurant team standing in front of the entrance"></div>
  <div class="feed-post">
    <div class="who">Teatro Lunaverde</div>
    <div class="when">on Tuesday</div>
    <div>There's a new chef in town!</div>
    <div>New at Teatro Lunaverde, a little piece of Italy in the centre of Amsterdam</div>
    <div class="gap">Come say hi to our team when you're around!</div>
  </div>
  <div class="feed-actions">19 likes &nbsp;&nbsp; Comment &nbsp;&nbsp; 3 shares</div>
</aside>

<footer class="site-footer">
  <div class="footer-brand">
    <span class="brand-dot"></span>
    <span class="brand-name">TEATRO LUNAVERDE</span>
  </div>
  <div class="footer-col abs" style="left:542px;top:42px">
    <h5>Address</h5>
    <p>Teatro Lunaverde<br>Lindengracht 42<br>1015KH Amsterdam<br>Tel nr: (+31) 20 555 0192</p>
    <span class="circle-icon"></span><span class="circle-icon"></span><span class="circle-icon"></span>
  </div>
  <div class="footer-col abs" style="left:805px;top:42px">
    <h5>Navigation</h5>
    <p style="line-height:19px">Home<br>Menu<br>Group Menu<br>Reservation<br>Contact Us</p>
  </div>
  <span class="footer-line"></span>
  <div class="copyright">Copyright teatrolunaverde.info. All Right Reserved.</div>
</footer>

</body>
</html>
```